" Um centro esportivo que possui diversas modalidades como circuito de areia, academia para idosos, futevôlei, academia personalizada e ginástica infantil. O Espaço Ritmo faz parte do Grupo Tolbra, uma empresa que presta serviços de assistência familiar e funeral na cidade de Sao Fidélis, interior do Rio de janeiro. Nosso espaço possui paisagismos com plantas visando o bem estar visual, suas cores predominantes sao o verde, branco e marrom. "

```html
<!DOCTYPE html>
<html lang="pt-BR">
<head>
<meta charset="utf-8">
<title>Espaço Ritmo – Cartão de visita</title>
<link rel="stylesheet" href="https://fonts.googleapis.com/css2?family=Mulish:wght@400;600;800&display=swap">
<style>
  :root {
    --green: #8dc63f;
    --grey-text: #6f6f6f;
    --paper: #ffffff;
    --backdrop: #ececec;
  }
  * { margin: 0; padding: 0; box-sizing: border-box; }
  html, body { width: 1200px; height: 1200px; overflow: hidden; }
  body {
    background: var(--backdrop);
    font-family: "Mulish", sans-serif;
    position: relative;
  }
  .card {
    position: absolute;
    left: 150px;
    width: 900px;
    height: 500px;
    border-radius: 34px;
    overflow: hidden;
    box-shadow: 0 6px 24px rgba(0,0,0,0.12);
  }
  .card-back { top: 60px; background: var(--green); }
  .card-back .writing-lines { position: absolute; inset: 0; width: 100%; height: 100%; }

  .card-front { top: 640px; background: var(--paper); }
  .card-front .edge-band { position: absolute; left: 0; top: 0; width: 60px; height: 100%; }

  .brand-name {
    position: absolute;
    left: 0;
    right: 0;
    top: 100px;
    text-align: center;
    color: var(--green);
    font-weight: 600;
    font-size: 54px;
    line-height: 1.15;
  }
  .brand-name span { display: block; }

  .contacts {
    position: absolute;
    top: 330px;
    font-size: 22px;
    color: var(--grey-text);
    line-height: 1.45;
  }
  .contacts-web { left: 120px; text-align: right; }
  .contacts-place { left: 510px; }
  .contact-row { display: flex; align-items: center; gap: 8px; }
  .contacts-web .contact-row { justify-content: flex-end; }
  .icon { width: 20px; height: 20px; flex: none; }
  .indent { padding-left: 28px; }
</style>
</head>
<body>

  <section class="card card-back" aria-label="Verso do cartão">
    <svg class="writing-lines" viewBox="0 0 900 500" preserveAspectRatio="none">
      <g stroke="#ffffff" stroke-width="2">
        <line x1="90" y1="70" x2="810" y2="70"/>
        <line x1="90" y1="120" x2="810" y2="120"/>
        <line x1="90" y1="170" x2="810" y2="170"/>
        <line x1="90" y1="220" x2="810" y2="220"/>
        <line x1="90" y1="270" x2="810" y2="270"/>
        <line x1="90" y1="320" x2="810" y2="320"/>
        <line x1="90" y1="370" x2="810" y2="370"/>
        <line x1="90" y1="420" x2="810" y2="420"/>
      </g>
    </svg>
  </section>

  <section class="card card-front" aria-label="Frente do cartão">
    <svg class="edge-band" viewBox="0 0 60 500" preserveAspectRatio="none">
      <path d="M0 0 H28 Q8 250 28 500 H0 Z" fill="var(--green)"/>
    </svg>

    <h1 class="brand-name">
      <span>Espaço Ritmo</span>
      <span>Grupo Tolbra</span>
    </h1>

    <div class="contacts contacts-web">
      <div class="contact-row">contato@espacoritmo.com
        <svg class="icon" viewBox="0 0 20 20"><path d="M2 5h16v10H2z M2 5l8 6 8-6" fill="none" stroke="var(--green)" stroke-width="2"/></svg>
      </div>
      <div class="contact-row">facebook.com/espacoritmo
        <svg class="icon" viewBox="0 0 20 20"><circle cx="10" cy="10" r="7.5" fill="none" stroke="var(--green)" stroke-width="2"/><path d="M6 10h8M10 2.5v15" stroke="var(--green)" stroke-width="1.6"/></svg>
      </div>
    </div>

    <div class="contacts contacts-place">
      <div class="contact-row">
        <svg class="icon" viewBox="0 0 20 20"><path d="M10 1.5a6 6 0 0 0-6 6c0 4.5 6 11 6 11s6-6.5 6-11a6 6 0 0 0-6-6z" fill="var(--green)"/><circle cx="10" cy="7.5" r="2.2" fill="#fff"/></svg>
        Rua das Palmeiras, 240 Centro
      </div>
      <div class="indent">São Fidélis&nbsp; RJ</div>
      <div class="contact-row">
        <svg class="icon" viewBox="0 0 20 20"><path d="M5 2l3 4-2 2c1 2.5 3.5 5 6 6l2-2 4 3-2 3C8 18 2 12 2 4z" fill="var(--green)"/></svg>
        22 3000-1000/22 3000-2000
      </div>
    </div>
  </section>

</body>
</html>
```